Business card design for sustainable building and development company

Need a business card design for a new sustainable building and real estate development company in the San Francisco Bay area. Name of company is "Norvale Advisors, LLC" and we provide "Sustainable building, energy and development services" for residential and non residential projects. We'd like the following colors used but not all area required: green, gray, blue. Design should communicate innovation, professionalism and sustainability. Our current website is www.norvale-advisors.example. Another possible design idea is to have the following listed on the back of the card:
Certified: TRAM QX, Leaf Mark Grader, VOLT Grader, EcoState Examiner, RDQ HX Building Analyst. Its not a must but could be text that could be used for back of card. Overall, we are open to a simple, clean design and or one with more text than usual for a card.

Industry/Entity Type

Real Estate

Contact Information for Business Card

Name on card: Dmitri L. Hasby
Title for Name: Principal + Founder
Phone: 555.418.2096
Email: dhasby@norvale-advisors.example
Website: www.norvale-advisors.example

Also, please add the following for address:
Harlow Point, Calverra

Requirements
Nice to have
• If you can integrate the outline of a skyline on the backside of the card and if it looks good, I would like to see the design
Should not have
• a barcode;

```html
<!DOCTYPE html>
<html lang="en">
<head>
<meta charset="utf-8">
<title>Norvale Advisors – Business Card</title>
<link href="https://fonts.googleapis.com/css2?family=Montserrat:wght@400;600&family=PT+Sans:wght@400;700&display=swap" rel="stylesheet">
<style>
  :root {
    --stage: #2b2e30;
    --lime: #78f90c;
    --lime-soft: #7ef514;
    --white: #ffffff;
    --paper: #f4f7f8;
    --band: #1f2a14;
    --ink: #1b1b1b;
  }
  html, body {
    margin: 0;
    width: 1106px;
    height: 1200px;
    overflow: hidden;
    background: var(--stage);
  }
  .canvas { position: relative; width: 1106px; height: 1200px; }
  .card {
    position: absolute;
    left: 191px;
    width: 600px;
    height: 352px;
    transform: scale(1.1766);
    transform-origin: 0 0;
    overflow: hidden;
  }
  .card--front { top: 127px; background: var(--white); }
  .card--back { top: 641px; height: 350px; background: linear-gradient(180deg, var(--white), var(--paper)); }

  /* front */
  .front__field {
    position: absolute; left: 7px; top: 7px; right: 7px; bottom: 7px;
    background: var(--lime);
  }
  .brand { position: absolute; left: 30px; top: 93px; display: flex; align-items: center; }
  .brand__mark {
    width: 88px; height: 88px; border-radius: 50%;
    border: 12px solid var(--white); box-sizing: border-box;
    margin-right: 44px;
  }
  .brand__name {
    font-family: "Montserrat", sans-serif; font-weight: 600;
    font-size: 41px; line-height: 1; color: var(--white); margin: 0;
    letter-spacing: -0.5px;
  }
  .brand__tagline {
    font-family: "Montserrat", sans-serif; font-weight: 400;
    font-size: 11.6px; color: var(--white); margin: 7px 0 0 1px;
    text-transform: uppercase; letter-spacing: 0.1px;
  }
  .front__band {
    position: absolute; left: 0; right: 0; top: 268px; height: 13px;
    background: var(--band);
  }
  .certs {
    position: absolute; left: 0; right: 0; top: 288px;
    font-family: "PT Sans", sans-serif; font-size: 12.5px; line-height: 17px;
    color: var(--ink); text-align: center; margin: 0;
  }

  /* back */
  .tab {
    position: absolute; top: 70px; width: 30px; height: 205px;
    background: var(--lime-soft);
  }
  .tab--left { left: 8px; border-radius: 0 22px 22px 0; }
  .tab--right { right: 5px; border-radius: 22px 0 0 22px; }
  .back__mark {
    position: absolute; left: 57px; top: 75px;
    width: 180px; height: 180px; border-radius: 50%;
    border: 16px solid var(--lime-soft); box-sizing: border-box;
  }
  .person { position: absolute; left: 287px; top: 107px; margin: 0; }
  .person__name {
    font-family: "PT Sans", sans-serif; font-weight: 700;
    font-size: 30px; line-height: 1; color: var(--lime-soft); margin: 0;
  }
  .person__title {
    font-family: "PT Sans", sans-serif; font-weight: 700;
    font-size: 19px; color: var(--lime-soft); margin: 5px 0 0;
  }
  .contact {
    position: absolute; left: 289px; top: 190px; margin: 0;
    font-family: "PT Sans", sans-serif; font-size: 12.6px; line-height: 16.6px; color: var(--ink);
    display: grid; grid-template-columns: 64px 13px auto;
  }
  .contact dt, .contact dd { margin: 0; white-space: nowrap; }
</style>
</head>
<body>
<div class="canvas">
  <section class="card card--front">
    <div class="front__field">
      <div class="brand">
        <div class="brand__mark"></div>
        <div>
          <h1 class="brand__name">Norvale Advisors</h1>
          <p class="brand__tagline">Resilient Building, Power &amp; Land Planning Services</p>
        </div>
      </div>
    </div>
    <div class="front__band"></div>
    <p class="certs">Certified:<br>TRAM QX, Leaf Mark Grader, VOLT Grader, EcoState Examiner, RDQ HX Building Analyst</p>
  </section>

  <section class="card card--back">
    <div class="tab tab--left"></div>
    <div class="tab tab--right"></div>
    <div class="back__mark"></div>
    <div class="person">
      <h2 class="person__name">Dmitri L. Hasby</h2>
      <p class="person__title">Principal / Owner</p>
    </div>
    <dl class="contact">
      <dt>Phone</dt><dd>:</dd><dd>555.418.2096</dd>
      <dt>Web</dt><dd>:</dd><dd>www.norvale-advisors.example</dd>
      <dt>Email</dt><dd>:</dd><dd>dhasby@norvale-advisors.example</dd>
      <dt>Address</dt><dd>:</dd><dd>Harlow Point, Calverra</dd>
    </dl>
  </section>
</div>
</body>
</html>
```